Kellwood Build, Carpentry Services

Business card for carpentry business in the Sunshine Coast.

Business card layout required using logo provided - provided both PDF copy and AI. Please let me know if you would like a the files for the logo symbol and text by itself.

Business Colours are grey, blue and white. The font colours codes for this design are Blue Hex # 00B4E6 and Hex # 39393B for the gray colour.

FYI font for logo is Gotham Bold.

Preference for a clean and striking layout that is simple and elegant.

Target Market(s)

Young Families, retirees, young couples requiring assistance with small to medium works/renovations on the Sunshine Coast.

Industry/Entity Type

Construction

Contact Information for Business Card

Dean Kellwood
Carpenter
0489305627
dean@kellwoodbuild.com.au
Coral Point, Seabright Coast
RHPA Licensed Carpenter (In smaller font)

Font styles to use
Sans Serif

Colors

Designer to choose colors to be used in the design.

Requirements
Must have
• Logo provided must appear on the card, preferably on one side of the card by itself with the text on the alternate side
Nice to have
• Text on the other side of card, maybe grey background and white font here but happy for the designer to provide ideas here.
Should not have
• Use of other colours, other than the ones provided - white, grey and blue. Black optional.

```html
<!DOCTYPE html>
<html lang="en">
<head>
<meta charset="utf-8">
<title>Kellwood Build – Business Card</title>
<link href="https://fonts.googleapis.com/css2?family=Montserrat:wght@300;400;700&display=swap" rel="stylesheet">
<style>
  :root {
    --blue: #00B4E6;
    --card-grey: #39393B;
    --backdrop: #1c1c1d;
    --white: #ffffff;
    --soft-white: #e9e9ea;
  }
  * { margin: 0; padding: 0; box-sizing: border-box; }
  html, body {
    width: 1200px; height: 1200px; overflow: hidden;
    background: var(--backdrop);
    font-family: "Montserrat", sans-serif;
  }
  .stage {
    position: relative; width: 1200px; height: 1200px;
    display: flex; flex-direction: column; align-items: center;
    justify-content: center; gap: 52px;
  }
  .card {
    position: relative; width: 900px; height: 514px;
    background: var(--card-grey);
    box-shadow: 0 14px 40px rgba(0,0,0,0.45);
  }
  .wordmark {
    display: flex; align-items: center; gap: 18px;
    color: var(--blue); font-weight: 700; text-transform: uppercase;
    letter-spacing: 0.04em; white-space: nowrap;
  }
  .wordmark-square { background: var(--blue); flex: none; }

  /* front */
  .card-front { display: flex; align-items: center; justify-content: center; }
  .card-front .wordmark { font-size: 50px; }
  .card-front .wordmark-square { width: 44px; height: 44px; }

  /* back */
  .card-back .wordmark {
    position: absolute; left: 92px; top: 110px; font-size: 50px;
  }
  .card-back .wordmark-square { width: 44px; height: 44px; }
  .divider {
    position: absolute; left: 100px; top: 302px;
    width: 560px; height: 2px; background: var(--blue);
  }
  .contact-list {
    position: absolute; left: 74px; top: 330px; list-style: none;
    color: var(--white); font-weight: 400; font-size: 23px; letter-spacing: 0.04em;
  }
  .contact-list li { display: flex; align-items: center; gap: 14px; height: 34px; }
  .contact-icon { width: 20px; height: 20px; flex: none; fill: var(--blue); }
  .person {
    position: absolute; right: 70px; top: 318px; text-align: right;
    text-transform: uppercase; font-weight: 700; letter-spacing: 0.06em;
  }
  .person-name { color: var(--white); font-size: 32px; }
  .person-role { color: var(--blue); font-size: 23px; margin-top: 2px; }
  .licence {
    position: absolute; right: 70px; bottom: 44px;
    color: var(--soft-white); font-size: 16px; font-weight: 400; letter-spacing: 0.05em;
  }
</style>
</head>
<body>
<main class="stage">
  <section class="card card-front" aria-label="Card front">
    <div class="wordmark"><span class="wordmark-square"></span><span>Kellwood Build</span></div>
  </section>

  <section class="card card-back" aria-label="Card back">
    <div class="wordmark"><span class="wordmark-square"></span><span>Kellwood Build</span></div>
    <div class="divider"></div>
    <ul class="contact-list">
      <li>
        <svg class="contact-icon" viewBox="0 0 24 24" aria-hidden="true"><path d="M6.6 10.8a15.1 15.1 0 0 0 6.6 6.6l2.2-2.2c.3-.3.7-.4 1-.2 1.1.4 2.3.6 3.6.6.6 0 1 .4 1 1V20c0 .6-.4 1-1 1A17 17 0 0 1 3 4c0-.6.4-1 1-1h3.5c.6 0 1 .4 1 1 0 1.3.2 2.5.6 3.6.1.3 0 .7-.2 1z"/></svg>
        <span>0489305627</span>
      </li>
      <li>
        <svg class="contact-icon" viewBox="0 0 24 24" aria-hidden="true"><path d="M2 5h20v14H2z M4 7v.4l8 5.2 8-5.2V7z" fill-rule="evenodd"/></svg>
        <span>dean@kellwoodbuild.com.au</span>
      </li>
      <li>
        <svg class="contact-icon" viewBox="0 0 24 24" aria-hidden="true"><path d="M12 2a7 7 0 0 0-7 7c0 5.2 7 13 7 13s7-7.8 7-13a7 7 0 0 0-7-7zm0 9.5a2.5 2.5 0 1 1 0-5 2.5 2.5 0 0 1 0 5z"/></svg>
        <span>Coral Point, Seabright Coast</span>
      </li>
    </ul>
    <div class="person">
      <p class="person-name">Dean Kellwood</p>
      <p class="person-role">Carpenter</p>
    </div>
    <p class="licence">RHPA Licensed Carpenter</p>
  </section>
</main>
</body>
</html>
```